Flyer Design Project

We are a restaurant meal delivery service. We deliver from a variety of restaurants. We would like a flyer that will promote our service to busy commuters. The flyer will be distributed at local train stations. I would like the flyer to say something like "What's for dinner?" or "Meet us at your place!" or anything that is catchy.
In the flyer we want the customer to order online at our website plumcartmeals.com and use coupon code $5off. Using the coupon code will get them $5 off of their online purchase.
We would like to pass the flyers out in the morning and have the customers go online either on the train or at work to schedule the food to be delivered for dinner.
Target Market(s)
Hungry commuters that are in a rush 30 - 50 women
Industry/Entity Type
Restaurant

```html
<!DOCTYPE html>
<html lang="en">
<head>
<meta charset="utf-8">
<title>Plumcart Meals – Online Ordering Flyer</title>
<link href="https://fonts.googleapis.com/css2?family=Open+Sans:wght@400;600;700;800&family=Kalam:wght@400&display=swap" rel="stylesheet">
<style>
  :root {
    --page-bg: #e6e1da;
    --brand-red: #b3141c;
    --deep-red: #7e0c12;
    --ink: #0b0b0b;
    --panel-gray: #58585b;
    --footer-gray: #5e5e61;
    --cream-top: #f3e8dc;
    --cream-bottom: #d8c0a5;
    --white: #ffffff;
    --text-dark: #1b1b1b;
    --coupon-yellow: #f4d21d;
    --photo-warm: #b8452a;
    --photo-light: #d9b27c;
    --photo-green: #5b7f2f;
  }
  * { box-sizing: border-box; margin: 0; padding: 0; }
  html, body { width: 975px; height: 1200px; overflow: hidden; }
  body { background: var(--page-bg); font-family: "Open Sans", Arial, sans-serif; position: relative; }

  .flyer {
    position: absolute; left: 83px; top: 26px; width: 810px; height: 1148px;
    background: var(--white); overflow: hidden;
    box-shadow: 0 6px 18px rgba(0,0,0,.25);
  }

  /* header */
  .header-art { position: absolute; left: 0; top: 0; width: 810px; height: 541px; }
  .brand { position: absolute; left: 22px; top: 190px; display: flex; align-items: center; gap: 10px; }
  .brand-dot { width: 22px; height: 22px; border-radius: 50%; background: var(--brand-red); flex: none; }
  .brand-name { font-weight: 800; font-size: 40px; line-height: 42px; color: var(--brand-red); letter-spacing: -0.5px; }

  .tagline {
    position: absolute; right: 24px; top: 178px; text-align: right;
    color: var(--white); font-weight: 700; font-size: 29px; line-height: 35px;
    text-shadow: 0 2px 3px rgba(0,0,0,.85);
  }
  .headline {
    position: absolute; left: -44px; width: 810px; top: 300px; text-align: center;
    color: var(--white); font-weight: 600; font-size: 45px; line-height: 54px;
  }
  .steps { position: absolute; left: 0; top: 430px; width: 810px; height: 100px; }
  .step { position: absolute; top: 0; height: 100px; display: flex; align-items: center; gap: 14px; }
  .step-num {
    width: 72px; height: 72px; border-radius: 50%; flex: none;
    background: radial-gradient(circle at 40% 35%, #e0363c, var(--brand-red) 60%, var(--deep-red));
    border: 3px solid #e9e9e9; color: var(--white);
    font-size: 46px; font-weight: 700; display: flex; align-items: center; justify-content: center;
  }
  .step-text { color: var(--white); font-weight: 700; font-size: 17px; line-height: 24px; }
  .step.third .step-text { line-height: 21px; }

  .rule-red { position: absolute; left: 0; top: 539px; width: 810px; height: 6px; background: var(--brand-red); }

  /* details */
  .info-panel {
    position: absolute; left: 0; top: 545px; width: 810px; height: 300px;
    background: var(--panel-gray);
  }
  .info-col { position: absolute; top: 0; color: var(--white); }
  .info-col.details { left: 54px; width: 300px; }
  .info-col.hours { left: 506px; width: 280px; }
  .script-title { font-family: "Kalam", cursive; font-size: 48px; line-height: 62px; margin-top: 6px; color: var(--white); }
  .bullet-list { list-style: none; font-size: 20px; line-height: 29px; }
  .details .bullet-list li.wrap { line-height: 24px; padding-top: 2px; padding-bottom: 3px; }
  .bullet-list li { position: relative; padding-left: 20px; }
  .bullet-list li::before {
    content: ""; position: absolute; left: 0; top: 11px; width: 10px; height: 10px;
    border: 1.5px solid var(--white); border-radius: 50%;
  }
  .bullet-list .plain { padding-left: 0; }
  .bullet-list .plain::before { display: none; }
  .bullet-list .indent { padding-left: 16px; }
  .bullet-list .indent::before { display: none; }
  .card-strip {
    position: absolute; left: 506px; top: 226px; width: 235px; height: 44px;
    background: var(--white); border: 1px solid #ccc; display: flex; gap: 6px; padding: 6px;
  }
  .card-strip span { flex: 1; border-radius: 2px; }
  .card-strip .c1 { background: #e9a23b; }
  .card-strip .c2 { background: #2a3f8f; }
  .card-strip .c3 { background: #3e6b3a; }
  .card-strip .c4 { background: #24468a; }

  /* add-ons */
  .addons {
    position: absolute; left: 0; top: 845px; width: 810px; height: 170px;
    background: linear-gradient(180deg, var(--cream-top), var(--cream-bottom));
  }
  .addons-title {
    position: absolute; left: 26px; top: 2px; font-family: "Kalam", cursive;
    font-size: 42px; line-height: 56px; color: var(--white);
  }
  .price-list { position: absolute; list-style: none; top: 44px; font-weight: 700; font-size: 18px; line-height: 26.5px; color: var(--text-dark); }
  .price-list.left { left: 26px; width: 295px; }
  .price-list.right { left: 470px; width: 312px; }
  .price-list li { display: flex; align-items: baseline; }
  .price-list li::before { content: ">"; color: var(--brand-red); margin-right: 12px; }
  .price-list .leader { flex: 1; border-bottom: 2px dotted var(--text-dark); margin: 0 2px 5px; }
  .price-list .price { color: var(--brand-red); }
  .price-list .note { display: block; font-size: 10.5px; line-height: 13px; padding-left: 22px; }
  .price-list .note::before { display: none; }
  .drinks-photo {
    position: absolute; left: 342px; top: 40px; width: 88px; height: 76px; border-radius: 6px;
    background: linear-gradient(90deg, #b01a1a, #d9d9d9 50%, #3b8a3f);
  }

  .slash-band { position: absolute; left: 0; top: 1000px; width: 810px; height: 40px; }

  /* footer */
  .footer { position: absolute; left: 0; top: 1030px; width: 810px; height: 118px; background: var(--footer-gray); }
  .coupon {
    position: absolute; left: 41px; top: 20px; width: 262px; height: 84px;
    border: 2px dashed var(--coupon-yellow); border-radius: 10px;
    color: var(--white); font-size: 18px; line-height: 25px; text-align: center; padding-top: 4px;
  }
  .coupon .code { color: var(--coupon-yellow); }
  .coupon .amount { color: var(--coupon-yellow); font-size: 25px; font-weight: 600; }
  .scissors { position: absolute; left: 30px; top: 2px; width: 44px; height: 34px; }
  .contact { position: absolute; right: 26px; top: 14px; text-align: right; color: var(--white); }
  .contact .more { font-size: 17px; line-height: 22px; }
  .contact .call, .contact .web { font-size: 17px; line-height: 22px; }
  .contact .call b, .contact .web b { color: var(--coupon-yellow); font-weight: 400; }
  .contact .disclaimer-title { font-size: 11px; font-weight: 700; margin-top: 4px; line-height: 14px; }
  .contact .disclaimer { font-size: 10.5px; line-height: 13px; }
</style>
</head>
<body>
<main class="flyer">

  <svg class="header-art" viewBox="0 0 810 541">
    <defs>
      <linearGradient id="foodGradient" x1="0" y1="0" x2="1" y2="1">
        <stop offset="0" stop-color="var(--photo-warm)"/>
        <stop offset="0.55" stop-color="#c86a3a"/>
        <stop offset="0.8" stop-color="var(--photo-light)"/>
        <stop offset="1" stop-color="var(--photo-green)"/>
      </linearGradient>
    </defs>
    <polygon points="231,0 810,0 810,450 350,225" fill="url(#foodGradient)" role="img" aria-label="Photo of plated restaurant dishes: grilled salmon with rice, wings and vegetables"/>
    <polyline points="350,225 810,450" stroke="#ffffff" stroke-width="6" fill="none"/>
    <polygon points="0,406 350,225 810,456 810,541 0,541" fill="var(--ink)"/>
  </svg>

  <div class="brand">
    <span class="brand-dot"></span>
    <span class="brand-name">Plumcart<br>Meals</span>
  </div>

  <p class="tagline">We Bring Your<br>Favorite Restaurants<br>Right to Your Door!</p>

  <h1 class="headline">Online<br>Ordering Instructions</h1>

  <div class="steps">
    <div class="step" style="left:24px;"><span class="step-num">1</span><span class="step-text">SELECT A<br>RESTAURANT</span></div>
    <div class="step" style="left:279px;"><span class="step-num">2</span><span class="step-text">CHOOSE<br>DELIVERY<br>TIME &amp; ITEMS</span></div>
    <div class="step third" style="left:535px;"><span class="step-num">3</span><span class="step-text">RELAX<br>YOUR MEAL WILL<br>ARRIVE AS<br>SCHEDULED</span></div>
  </div>

  <div class="rule-red"></div>

  <section class="info-panel">
    <div class="info-col details">
      <h2 class="script-title">Details</h2>
      <ul class="bullet-list">
        <li>$15 Minimum Order</li>
        <li>Delivery $3.99</li>
        <li class="wrap">Prices and menu items are subject to change without notice</li>
        <li>Company Checks OK</li>
        <li>All Credit Cards are accepted</li>
      </ul>
    </div>
    <div class="info-col hours">
      <h2 class="script-title">Hours</h2>
      <ul class="bullet-list">
        <li class="plain">Call Center Hours</li>
        <li>Mon-Fri</li>
        <li class="indent">Lunch - 11am - 2pm</li>
        <li class="indent">Dinner - 4pm - 9pm</li>
        <li>Sat-Sun - 5pm - 9pm</li>
      </ul>
    </div>
    <div class="card-strip" role="img" aria-label="Accepted payment cards">
      <span class="c1"></span><span class="c2"></span><span class="c3"></span><span class="c4"></span>
    </div>
  </section>

  <section class="addons">
    <h2 class="addons-title">Add-ons</h2>
    <ul class="price-list left">
      <li>Fizzo Cola - 12oz<span class="leader"></span><span class="price">$0.75</span></li>
      <li>Fizzo Cola - 6-pack<span class="leader"></span><span class="price">$4.25</span></li>
      <li>Diet Fizzo - 12oz<span class="leader"></span><span class="price">$0.75</span></li>
      <li>Diet Fizzo - 6-pack<span class="leader"></span><span class="price">$4.25</span></li>
    </ul>
    <div class="drinks-photo" role="img" aria-label="Photo of three soda cans"></div>
    <ul class="price-list right">
      <li>Plates<span class="leader"></span><span class="price">$.20 per</span></li>
      <li>Cups<span class="leader"></span><span class="price">$.15 per</span></li>
      <li>Plastic ware<span class="leader"></span><span class="price">$.25 per</span></li>
      <li class="note">(Includes knife, fork, spoon, napkin and salt &amp; pepper)</li>
    </ul>
  </section>

  <svg class="slash-band" viewBox="0 0 810 40" preserveAspectRatio="none" aria-hidden="true">
    <polygon points="0,6 810,0 810,22 0,30" fill="var(--brand-red)"/>
    <polygon points="0,24 810,18 810,26 0,34" fill="var(--deep-red)"/>
  </svg>

  <footer class="footer">
    <div class="coupon">
      Using this coupon code<br>
      <span class="code">$5off</span> &amp; get <span class="amount">$5</span> off on<br>
      online purchase
    </div>
    <svg class="scissors" viewBox="0 0 44 34" aria-hidden="true">
      <circle cx="8" cy="8" r="6" fill="none" stroke="var(--coupon-yellow)" stroke-width="3"/>
      <circle cx="8" cy="26" r="6" fill="none" stroke="var(--coupon-yellow)" stroke-width="3"/>
      <line x1="13" y1="11" x2="42" y2="24" stroke="var(--coupon-yellow)" stroke-width="3"/>
      <line x1="13" y1="23" x2="42" y2="10" stroke="var(--coupon-yellow)" stroke-width="3"/>
    </svg>
    <div class="contact">
      <p class="more">FOR MORE DETAILS</p>
      <p class="web"><b>Order Online:</b> plumcartmeals.com</p>
      <p class="call"><b>Call Us Now:</b> (855) 555-0142</p>
      <p class="disclaimer-title">Plumcart Disclaimer</p>
      <p class="disclaimer">Food Photography may not be affiliated with any restaurant.</p>
    </div>
  </footer>

</main>
</body>
</html>
```